Informational Business Handout needs Company Information

We have this informational handout that we would like to start handing out to clients; however, the original designer failed to include any of our company contact information. Our main request is that you redesign this card with the appropriate contact information as listed below. We would like the information/content that is currently on the card to be on the new design as well. Feel free to take liberty with the rest of the card design, or not. Please see the card specifications and our company contact information below.

Card details: 7 x 5 inches (17.78 x 12.5 cm). Cardstock.

Company Contact Details:
Dorian Welkett, JD
TarnwickLaw, PLLC
482 E. Marlowe Ave, Ste. 310, Brennport, ID 83999
hello@tarnwicklaw-mail.com
(208) 555-0147

```html
<!DOCTYPE html>
<html lang="en">
<head>
<meta charset="utf-8">
<title>First-Party Special Needs Trust Handout – TarnwickLaw</title>
<link href="https://fonts.googleapis.com/css2?family=Montserrat:wght@400;600;700;800;900&display=swap" rel="stylesheet">
<style>
  :root {
    --navy: #0d2a66;
    --navy-band: #0a2a5e;
    --ink: #3c3c3c;
    --orange: #d4502a;
    --paper: #ffffff;
    --backdrop: #3a3a3a;
  }
  * { box-sizing: border-box; margin: 0; padding: 0; }
  html, body {
    width: 1200px; height: 1200px; overflow: hidden;
    background: var(--backdrop);
    font-family: "Montserrat", Arial, sans-serif;
  }
  .handout {
    position: absolute; left: 37px; top: 204px;
    width: 1132px; height: 796px;
    background: var(--paper);
    overflow: hidden;
  }
  .headline {
    position: absolute; left: 57px; top: 44px;
    color: var(--navy); font-weight: 900;
    font-size: 44px; line-height: 43px; letter-spacing: 0.2px;
    text-transform: uppercase; white-space: nowrap;
  }
  .lead {
    position: absolute; left: 59px; top: 150px;
    color: var(--ink); font-weight: 600;
    font-size: 23.5px; line-height: 28px; white-space: nowrap;
  }
  .subhead {
    position: absolute; left: 58px; top: 251px;
    color: var(--navy); font-weight: 900; font-size: 30px; line-height: 36px;
  }
  .checklist { list-style: none; }
  .checklist li {
    position: absolute; left: 58px;
    padding-left: 39px;
    color: var(--ink); font-weight: 600;
    font-size: 20.5px; line-height: 21.5px; white-space: nowrap;
  }
  .checklist li::before {
    content: ""; position: absolute; left: 0; top: 0;
    width: 24px; height: 24px;
    border: 3px solid var(--navy); border-radius: 6px;
  }
  .checklist li.two::before { top: 8px; }
  .checklist li.three::before { top: 6px; }
  .item-1 { top: 301px; }
  .item-2 { top: 337px; }
  .item-3 { top: 388px; }
  .item-4 { top: 423px; }
  .item-5 { top: 474px; }
  .item-6 { top: 509px; }
  .firm-name {
    position: absolute; left: 714px; top: 458px; width: 380px;
    text-align: center;
    color: var(--navy); font-weight: 700;
    font-size: 34px; letter-spacing: 5px;
  }
  .closing {
    position: absolute; left: 54px; top: 597px;
    color: var(--navy); font-weight: 700;
    font-size: 19.8px; line-height: 20px; white-space: nowrap;
  }
  .rule {
    position: absolute; left: 0; top: 671px; width: 100%; height: 10px;
    background: linear-gradient(90deg, var(--orange) 0%, var(--orange) 45%, var(--navy-band) 80%);
  }
  .contact-band {
    position: absolute; left: 0; top: 681px; width: 100%; height: 115px;
    background: var(--navy-band); color: #fff;
    font-weight: 400; font-size: 21px; line-height: 24px; white-space: nowrap;
  }
  .contact-name { position: absolute; left: 180px; top: 18px; }
  .contact-address { position: absolute; left: 204px; top: 47px; }
  .contact-phone { position: absolute; left: 671px; top: 36px; }
  .contact-email { position: absolute; left: 673px; top: 71px; }
  .icon { position: absolute; }
</style>
</head>
<body>
  <main class="handout">
    <h1 class="headline">Is a First-Party Special<br>Needs Trust Right for You?</h1>

    <p class="lead">Do you have a recognized disability by the Social Security Administration<br>which can be expected to result in death or which has lasted or can be<br>expected to last for a continuous period of not less than twelve months?</p>

    <h2 class="subhead">ARE YOU...</h2>

    <ul class="checklist">
      <li class="item-1">Under age 65?</li>
      <li class="item-2 two">Expecting settlement proceeds from the negligent<br>actions of a third party?</li>
      <li class="item-3">Expecting an inheritance?</li>
      <li class="item-4 two">Currently receiving, or will be applying for Social<br>Security income?</li>
      <li class="item-5">Currently receiving, or will be applying for Medicaid?</li>
      <li class="item-6 three">Wanting to maintain or qualify for Social Security<br>Income and/or medicaid after being awarded your<br>settlement or inheritance?</li>
    </ul>

    <div class="firm-name">TARNWICKLAW</div>

    <p class="closing">If you have a recognized disability and you answered yes to any of these questions,<br>you should contact our office to discuss whether a First-Party Special Needs Trust is right for you.</p>

    <div class="rule"></div>

    <footer class="contact-band">
      <div class="contact-name">Dorian Welkett, JD | TarnwickLaw, PLLC</div>
      <svg class="icon" style="left:177px;top:54px" width="20" height="27" viewBox="0 0 20 27" aria-hidden="true">
        <path d="M10 1a8.5 8.5 0 0 0-8.5 8.5C1.5 16 10 26 10 26s8.5-10 8.5-16.5A8.5 8.5 0 0 0 10 1z" fill="none" stroke="#d4502a" stroke-width="3"/>
        <circle cx="10" cy="9.5" r="3" fill="none" stroke="#d4502a" stroke-width="2.5"/>
      </svg>
      <div class="contact-address">482 E. Marlowe Ave,<br>Ste. 310, Brennport, ID 83999</div>

      <svg class="icon" style="left:640px;top:37px" width="24" height="24" viewBox="0 0 24 24" aria-hidden="true">
        <path d="M6.6 10.8a15.2 15.2 0 0 0 6.6 6.6l2.2-2.2a1 1 0 0 1 1-.25 11.4 11.4 0 0 0 3.6.57 1 1 0 0 1 1 1V20a1 1 0 0 1-1 1A17 17 0 0 1 3 4a1 1 0 0 1 1-1h3.5a1 1 0 0 1 1 1c0 1.25.2 2.45.57 3.57a1 1 0 0 1-.25 1z" fill="#d4502a"/>
      </svg>
      <div class="contact-phone">(208) 555-0147</div>

      <svg class="icon" style="left:642px;top:75px" width="22" height="16" viewBox="0 0 22 16" aria-hidden="true">
        <rect x="0" y="0" width="22" height="16" fill="#d4502a"/>
        <path d="M1 1l10 8 10-8M1 15l7-6M21 15l-7-6" fill="none" stroke="#0a2a5e" stroke-width="1.8"/>
      </svg>
      <div class="contact-email">hello@tarnwicklaw-mail.com</div>
    </footer>
  </main>
</body>
</html>
```